Business Card Design Project

I need a cool business card design for the company that will build residential houses.
The card should include:
1) Name: Boris Kalinov
2) Cell: 587.204.XXXX
3) Email: bor.kalinov@qwvend.example
4) Position: General Manager
5) Residential Home Building
6) Company logo that I have uploaded

Industry/Entity Type

Residential

```html
<!DOCTYPE html>
<html lang="en">
<head>
<meta charset="utf-8">
<title>Varenko Developments – Business Card</title>
<link href="https://fonts.googleapis.com/css2?family=Comfortaa:wght@400&display=swap" rel="stylesheet">
<style>
  :root {
    --page-bg: #e9e6e2;
    --front-light: #fafafa;
    --front-edge: #d9d9d9;
    --navy-band: #15205a;
    --back-bg: #2e3c77;
    --back-edge: #283569;
    --back-column: #233062;
    --brand-blue: #1f4fa3;
    --white: #ffffff;
  }
  html, body {
    margin: 0;
    padding: 0;
    width: 1200px;
    height: 1181px;
    overflow: hidden;
    background: var(--page-bg);
    font-family: "Comfortaa", sans-serif;
  }
  .canvas {
    position: relative;
    width: 1200px;
    height: 1181px;
  }
  .card {
    position: absolute;
    left: 256px;
    width: 688px;
    height: 395px;
    border-radius: 28px;
    overflow: hidden;
    box-shadow: 0 6px 14px rgba(0,0,0,0.25);
  }
  .card-front {
    top: 136px;
    background: radial-gradient(ellipse at 50% 55%, var(--front-light) 0%, #eeeeee 45%, var(--front-edge) 100%);
  }
  .brand-lockup {
    position: absolute;
    top: 330px;
    left: 0;
    width: 100%;
    transform: translateY(-136px);
    display: flex;
    align-items: center;
    justify-content: center;
    gap: 16px;
  }
  .brand-mark {
    width: 44px;
    height: 44px;
    border-radius: 50%;
    background: var(--brand-blue);
  }
  .brand-name {
    color: var(--brand-blue);
    font-size: 30px;
    line-height: 1.25;
    letter-spacing: 2px;
    text-align: left;
  }
  .front-band {
    position: absolute;
    left: 0;
    bottom: 0;
    width: 100%;
    height: 31px;
    background: var(--navy-band);
    color: var(--white);
    font-size: 16px;
    line-height: 31px;
    text-align: center;
  }
  .card-back {
    top: 640px;
    background: linear-gradient(90deg, var(--back-edge) 0%, var(--back-bg) 35%, var(--back-bg) 65%, var(--back-edge) 100%);
  }
  .back-column {
    position: absolute;
    left: 233px;
    width: 221px;
    background: var(--back-column);
  }
  .back-column-top { top: 0; height: 160px; }
  .back-column-bottom { top: 231px; height: 164px; }
  .holder {
    position: absolute;
    top: 170px;
    left: 0;
    width: 100%;
    text-align: center;
    color: var(--white);
  }
  .holder-name { font-size: 27px; line-height: 32px; }
  .holder-role { font-size: 16px; line-height: 18px; }
  .contact-mark {
    position: absolute;
    top: 266px;
    left: 313px;
    width: 64px;
    height: 64px;
    border-radius: 50%;
    background: var(--white);
  }
  .contact {
    position: absolute;
    top: 358px;
    left: 233px;
    width: 221px;
    text-align: center;
    color: var(--white);
    font-size: 12px;
    line-height: 16px;
  }
</style>
</head>
<body>
<main class="canvas">
  <section class="card card-front">
    <div class="brand-lockup">
      <span class="brand-mark"></span>
      <span class="brand-name">VARENKO<br>DEVELOPMENTS</span>
    </div>
    <div class="front-band">Residential Home Building</div>
  </section>

  <section class="card card-back">
    <div class="back-column back-column-top"></div>
    <div class="back-column back-column-bottom"></div>
    <div class="holder">
      <div class="holder-name">Boris Kalinov</div>
      <div class="holder-role">General Manager</div>
    </div>
    <span class="contact-mark"></span>
    <div class="contact">
      <div class="contact-phone">587.204.XXXX</div>
      <div class="contact-email">bor.kalinov@qwvend.example</div>
    </div>
  </section>
</main>
</body>
</html>
```